Astrology Reading Website to attract clients

I need a website for my astrology practice. My business name is Willow Tide Astrology. I will need a page the following pages: About, Readings, Booking, Contact, and Blog. I will need full figma or figma-like mockups of pages along with assets. I will need both desktop and mobile designs.
I like creams, dark blues and greens. I am fine with planets or other astrology symbolism.

Target Market(s)

new age, spiritual

Industry/Entity Type

Holistic, spiritual

Number of Pages Required

3 page

Colors
0054AA
0677BA
7BADD7
CADEEF
E8F1F8

Requirements
Nice to have
• calm and grounded backgrounds

```html
<!DOCTYPE html>
<html lang="en">
<head>
<meta charset="UTF-8">
<title>Willow Tide Astrology</title>
<link rel="stylesheet" href="https://fonts.googleapis.com/css2?family=Poiret+One&display=swap">
<style>
  :root {
    --curtain-deep: #0a2f66;
    --curtain-mid: #0054aa;
    --curtain-light: #0677ba;
    --seam: #061d42;
    --text-light: #e8f1f8;
    --button-fill: rgba(202, 222, 239, 0.28);
    --button-text: #f4f8fc;
  }
  * { margin: 0; padding: 0; box-sizing: border-box; }
  html, body {
    width: 1200px;
    height: 599px;
    overflow: hidden;
  }
  .hero {
    position: relative;
    width: 1200px;
    height: 599px;
    overflow: hidden;
  }
  .hero-backdrop {
    position: absolute;
    inset: 0;
    background:
      radial-gradient(ellipse at 50% 45%, var(--curtain-light) 0%, var(--curtain-mid) 50%, var(--curtain-deep) 100%);
  }
  .curtain-seam {
    position: absolute;
    top: 0;
    left: 590px;
    width: 3px;
    height: 100%;
    background: var(--seam);
    opacity: 0.7;
    -webkit-mask-image: linear-gradient(to bottom, #000 0, #000 170px, transparent 200px, transparent 450px, #000 480px, #000 100%);
    mask-image: linear-gradient(to bottom, #000 0, #000 170px, transparent 200px, transparent 450px, #000 480px, #000 100%);
  }
  .hero-content {
    position: absolute;
    inset: 0;
    z-index: 1;
    display: flex;
    flex-direction: column;
    align-items: center;
    margin-left: -18px;
  }
  .hero-title {
    margin-top: 196px;
    font-family: "Poiret One", sans-serif;
    font-weight: 400;
    font-size: 44px;
    line-height: 48px;
    letter-spacing: -0.5px;
    text-align: center;
    color: var(--text-light);
    text-transform: uppercase;
  }
  .hero-cta {
    margin-top: 84px;
    width: 156px;
    height: 38px;
    border-radius: 19px;
    background: var(--button-fill);
    color: var(--button-text);
    font-family: "Poiret One", sans-serif;
    font-size: 13px;
    letter-spacing: 0.2px;
    text-transform: uppercase;
    text-decoration: none;
    display: flex;
    align-items: center;
    justify-content: center;
  }
</style>
</head>
<body>
  <main class="hero">
    <div class="hero-backdrop" role="img" aria-label="Deep blue velvet stage curtain backdrop"></div>
    <div class="curtain-seam"></div>
    <div class="hero-content">
      <h1 class="hero-title">Your destiny,<br>written in the stars</h1>
      <a class="hero-cta" href="#readings">Step inside</a>
    </div>
  </main>
</body>
</html>
```